Tirolex

We need a business card for our company is a holding for different business all are different we try to have some air of relax and fun in our projects we add pictures of the office to give you an idea od the mood of the business

Business

```html
<!DOCTYPE html>
<html lang="en">
<head>
<meta charset="utf-8">
<title>Tirolex – Business Card</title>
<link href="https://fonts.googleapis.com/css2?family=Play:wght@400;700&display=swap" rel="stylesheet">
<style>
  :root {
    --page-bg: #d6d0c8;
    --card-top: #f1eee9;
    --card-bottom: #e2dcd3;
    --ink-dark: #3b3431;
    --ink-brown: #6a4b33;
    --brand-yellow: #f5e63a;
    --brand-brown: #6b4a2e;
    --rule: #9a958f;
    --icon: #5b4a3f;
  }
  * { margin: 0; padding: 0; box-sizing: border-box; }
  html, body {
    width: 1200px; height: 768px; overflow: hidden;
    background: var(--page-bg);
    font-family: "Play", sans-serif;
  }
  .canvas { position: relative; width: 1200px; height: 768px; }
  .card {
    position: absolute; left: 110px; top: 97px;
    width: 980px; height: 574px;
    border-radius: 26px; overflow: hidden;
    background: linear-gradient(160deg, var(--card-top), var(--card-bottom));
    box-shadow: 0 10px 30px rgba(0,0,0,.15);
    color: var(--ink-dark);
  }
  .brand {
    position: absolute; right: 40px; top: 120px;
    display: flex; align-items: center; gap: 14px;
  }
  .brand-mark { width: 34px; height: 34px; background: var(--brand-yellow); }
  .brand-name { font-size: 48px; font-weight: 700; color: var(--brand-brown); letter-spacing: 1px; }
  .holder-name {
    position: absolute; left: 42px; top: 196px;
    font-size: 27px; letter-spacing: 1.5px; text-transform: uppercase;
  }
  .holder-role {
    position: absolute; left: 42px; top: 244px;
    font-size: 21px; color: var(--ink-brown); letter-spacing: .5px;
  }
  .divider {
    position: absolute; left: 60px; top: 282px; width: 860px; height: 3px;
    background: linear-gradient(90deg, rgba(154,149,143,0), var(--rule) 15%, var(--rule) 70%, rgba(154,149,143,0));
  }
  .address {
    position: absolute; left: 42px; top: 372px;
    font-size: 22px; line-height: 33px; letter-spacing: 1px;
  }
  .contacts {
    position: absolute; right: 30px; top: 305px;
    list-style: none; text-align: right;
  }
  .contacts li {
    display: flex; justify-content: flex-end; align-items: center; gap: 12px;
    font-size: 20px; letter-spacing: 1.5px; height: 30px;
  }
  .contacts li.phone { margin-bottom: 18px; }
  .contacts li.online { font-size: 18px; letter-spacing: 1px; margin-bottom: 4px; }
  .contacts svg { width: 22px; height: 22px; fill: none; stroke: var(--icon); stroke-width: 1.8; }
  .footer-band {
    position: absolute; left: 0; bottom: 0; width: 980px; height: 64px;
  }
  .footer-web {
    position: absolute; left: 42px; bottom: 22px;
    font-size: 19px; letter-spacing: 1px; color: var(--ink-dark);
  }
</style>
</head>
<body>
<main class="canvas">
  <section class="card">
    <div class="brand">
      <span class="brand-mark"></span>
      <span class="brand-name">Tirolex</span>
    </div>

    <h1 class="holder-name">Marco Velden</h1>
    <p class="holder-role">Managing Director</p>
    <div class="divider"></div>

    <p class="address">214.9th floor,Quay<br>Weston Park Road TRX</p>

    <ul class="contacts">
      <li class="phone">024 681 3579
        <svg viewBox="0 0 24 24"><path d="M5 3h4l2 5-2.5 1.5a11 11 0 0 0 6 6L16 13l5 2v4a2 2 0 0 1-2 2A16 16 0 0 1 3 5a2 2 0 0 1 2-2z"/></svg>
      </li>
      <li class="phone">024 681 3579
        <svg viewBox="0 0 24 24"><rect x="7" y="2" width="10" height="20" rx="2"/><line x1="11" y1="18" x2="13" y2="18"/></svg>
      </li>
      <li class="phone">024 681 3579
        <svg viewBox="0 0 24 24"><rect x="4" y="8" width="8" height="13"/><rect x="12" y="3" width="8" height="18"/><line x1="15" y1="7" x2="17" y2="7"/><line x1="15" y1="11" x2="17" y2="11"/><line x1="15" y1="15" x2="17" y2="15"/><line x1="7" y1="12" x2="9" y2="12"/><line x1="7" y1="16" x2="9" y2="16"/></svg>
      </li>
      <li class="online">hello@tirolex.com
        <svg viewBox="0 0 24 24"><rect x="3" y="6" width="18" height="12"/><polyline points="3,6 12,13 21,6"/></svg>
      </li>
      <li class="online">www.tirolexgroup.com
        <svg viewBox="0 0 24 24"><circle cx="12" cy="12" r="9"/><ellipse cx="12" cy="12" rx="4" ry="9"/><line x1="3" y1="12" x2="21" y2="12"/></svg>
      </li>
    </ul>

    <svg class="footer-band" viewBox="0 0 980 64" preserveAspectRatio="none">
      <rect x="395" y="21" width="585" height="43" fill="var(--brand-brown)"/>
      <path d="M0 0 H375 Q402 0 412 30 L424 64 H0 Z" fill="var(--brand-yellow)"/>
      <path d="M375 0 Q402 0 412 30 L424 64" fill="none" stroke="#b8b2aa" stroke-width="3"/>
    </svg>
    <p class="footer-web">www.tirolexgroup.com</p>
  </section>
</main>
</body>
</html>
```